Design The Loomfield Hompage

See powerpoint

Industry/Entity Type

SAAS data product

Coding

Coded - Design and coding required

Number of Pages Required

4 page

Font styles to use
Sans Serif

```html
<!DOCTYPE html>
<html lang="en">
<head>
<meta charset="utf-8">
<title>The Loomfield — Public data for developers</title>
<link href="https://fonts.googleapis.com/css2?family=Roboto:wght@300;400;500;700&display=swap" rel="stylesheet">
<style>
:root{
  --navy:#0c2d62;
  --blue:#1a9ae6;
  --blue-dark:#0f5fc4;
  --blue-light:#4fbdf0;
  --hero-bg:#eaf6fd;
  --text:#3b4656;
  --muted:#5d6878;
  --orange:#f7941d;
  --dark-icon:#2b3550;
  --ring:#b9cbe0;
  --white:#ffffff;
}
*{margin:0;padding:0;box-sizing:border-box}
html,body{width:1200px;height:2667px;overflow:hidden}
body{position:relative;font-family:'Roboto',sans-serif;color:var(--text);background:var(--white)}
.abs{position:absolute}
a{text-decoration:none;color:inherit}

/* hero */
.hero-bg{left:0;top:0;width:1200px;height:600px;background:var(--hero-bg)}
.hero-wave{left:0;top:560px}
.logo{left:112px;top:32px;font-size:25px;color:var(--navy);font-weight:400}
.logo b{color:var(--blue);font-weight:500}
.nav{left:469px;top:39px;display:flex;gap:27px;font-size:15px;font-weight:500;color:var(--navy)}
.nav .active{color:var(--blue)}
.btn-pill{display:flex;align-items:center;justify-content:center;border-radius:30px;color:var(--white);font-weight:500}
.btn-signup{left:883px;top:32px;width:96px;height:36px;font-size:14px;background:linear-gradient(90deg,var(--blue-dark),var(--blue-light))}
.btn-login{left:992px;top:32px;width:97px;height:36px;font-size:14px;background:var(--orange)}
.hero-title{left:108px;top:160px;font-size:41px;line-height:48px;color:var(--navy);font-weight:400}
.hero-title strong{display:block;color:var(--blue);font-weight:700}
.hero-copy{left:112px;top:278px;width:416px;font-size:15px;line-height:24px;color:var(--text);font-weight:500}
.hero-copy p+p{margin-top:10px}
.btn-register{left:112px;top:418px;width:234px;height:52px;font-size:15px;background:linear-gradient(90deg,var(--blue-dark),var(--blue-light))}
.hero-art{left:631px;top:124px;width:540px;height:410px;border-radius:24px;background:radial-gradient(circle at 50% 55%,#cfe6f7 0%,#e3f1fb 55%,rgba(234,246,253,0) 75%)}
.dots{left:565px;top:529px;display:flex;gap:9px;align-items:center}
.dots span{width:8px;height:8px;border-radius:50%;background:#c6d3e0}
.dots .on{width:16px;height:16px;border:2px solid var(--blue);background:var(--white);position:relative}
.dots .on::after{content:"";position:absolute;left:3px;top:3px;width:6px;height:6px;border-radius:50%;background:var(--blue)}

/* features */
.section-title{left:0;width:1200px;text-align:center;font-size:40px;font-weight:400;color:var(--blue)}
.section-title b{color:var(--navy);font-weight:700}
.underline{left:568px;width:64px;height:3px;background:var(--blue)}
.intro{left:210px;top:804px;width:780px;text-align:center;font-size:14.5px;line-height:24px;color:var(--muted)}
.feat-icon{width:72px;height:72px;border-radius:50%;display:flex;align-items:center;justify-content:center}
.feat-icon.light{background:linear-gradient(135deg,var(--blue-light),var(--blue))}
.feat-icon.dark{background:var(--dark-icon)}
.feat h3{font-size:17px;font-weight:500;color:var(--navy);margin-bottom:8px}
.feat p{font-size:13.8px;line-height:21px;color:var(--muted)}
.feat.right{text-align:right}
.center-art{left:430px;top:922px;width:340px;height:340px;border-radius:50%;background:radial-gradient(circle at 50% 45%,#e8e6f6 0%,#cfdcec 60%,#bccde3 100%)}
.btn-start{left:502px;top:1363px;width:195px;height:48px;font-size:15px;background:linear-gradient(90deg,var(--blue-dark),var(--blue-light))}

/* blog */
.blog-bg{left:0;top:1506px;width:1200px;height:640px;background:linear-gradient(180deg,#eaf5fd 0%,#ffffff 100%)}
.card{width:320px;height:346px;top:1657px;background:var(--white);border:2px solid #d7e6f3;border-radius:6px;overflow:hidden}
.card .photo{height:209px;background:linear-gradient(135deg,#223a5e,#0f1c33)}
.card .photo.warm{background:linear-gradient(135deg,#3b3a3f,#7a5a2a 55%,#1c1c22)}
.card .photo.cool{background:linear-gradient(135deg,#10264a,#2a5597 55%,#0c1a33)}
.card .body{padding:18px 10px 0 19px}
.card time{display:block;font-size:13.5px;line-height:16px;color:var(--navy)}
.card h4{margin-top:9px;font-size:14.8px;line-height:22px;font-weight:500;color:#111a2b;white-space:nowrap}
.card .more{display:flex;align-items:center;gap:6px;margin-top:12px;font-size:12.5px;font-weight:700;color:var(--blue);letter-spacing:.3px}

/* footer */
.footer-shape{left:0;top:2150px}
.newsletter{left:112px;top:2108px;width:976px;height:173px;border-radius:8px;background:linear-gradient(90deg,#fdb304 0%,#f7941d 50%,#ef7a30 100%)}
.newsletter h2{position:absolute;left:72px;top:44px;font-size:35px;line-height:47px;font-weight:700;color:var(--white)}
.subscribe{position:absolute;left:388px;top:59px;width:514px;height:57px;border-radius:30px;background:var(--white)}
.subscribe span{position:absolute;left:30px;top:19px;font-size:15px;color:#6b7380}
.subscribe b{position:absolute;right:8px;top:7px;width:140px;height:43px;border-radius:24px;background:linear-gradient(90deg,var(--blue-dark),var(--blue));color:var(--white);font-size:15px;display:flex;align-items:center;justify-content:center;letter-spacing:.5px}
.f-brand{left:100px;top:2380px;width:286px;text-align:center;color:var(--white)}
.f-brand h5{font-size:26px;font-weight:400}
.f-brand h5 b{font-weight:700}
.f-brand p{margin-top:14px;font-size:14.5px;line-height:21px;text-align:justify;text-align-last:center}
.f-divider{top:2341px;width:1px;height:190px;background:rgba(255,255,255,.35)}
.f-col{top:2359px;color:var(--white)}
.f-col h6{font-size:17px;font-weight:500;position:relative;padding-left:34px}
.f-col h6::before{content:"";position:absolute;left:0;top:2px;width:3px;height:18px;background:var(--white)}
.f-col ul{list-style:none;margin-top:17px;padding-left:35px}
.f-col li{font-size:14px;line-height:26px;color:rgba(255,255,255,.8)}
.f-col .mail{font-size:15px;color:var(--white);font-weight:500}
.social{display:flex;gap:10px;margin-top:14px;padding-left:35px}
.social span{width:16px;height:16px;border-radius:50%;background:var(--white)}
.f-rule{left:0;top:2585px;width:1200px;height:1px;background:rgba(255,255,255,.3)}
.copyright{left:0;top:2614px;width:1200px;text-align:center;font-size:14px;color:rgba(255,255,255,.85)}
</style>
</head>
<body>

<!-- Hero -->
<div class="abs hero-bg"></div>
<svg class="abs hero-wave" width="1200" height="110" viewBox="0 0 1200 110">
  <path d="M0 0 L1200 0 L1200 30 C1120 70 1020 90 900 60 C760 25 620 -5 470 30 C300 70 150 80 0 20 Z" fill="#eaf6fd"/>
  <path d="M0 30 C150 90 300 80 470 40 C620 5 760 30 900 70 C1020 100 1120 80 1200 40 L1200 110 L0 110 Z" fill="#d6ecf8"/>
  <path d="M0 45 C150 100 300 90 470 52 C620 20 760 45 900 85 C1020 115 1120 95 1200 60 L1200 110 L0 110 Z" fill="#ffffff"/>
</svg>

<div class="abs logo">The <b>Loomfield</b></div>
<nav class="abs nav">
  <a class="active">Home</a><a>Pricing</a><a>Documentation</a><a>Data</a><a>Blog</a>
</nav>
<a class="abs btn-pill btn-signup">Sign-Up</a>
<a class="abs btn-pill btn-login">Login</a>

<h1 class="abs hero-title">The Loomfield collects <strong>many public data sources</strong></h1>
<div class="abs hero-copy">
  <p>From demographics to economics, from weather to health, on country level or community level.</p>
  <p>The Loomfield collects many public data sources and organizes it for you.</p>
</div>
<a class="abs btn-pill btn-register">Register and start for free</a>
<div class="abs hero-art" role="img" aria-label="Isometric illustration of servers, charts, a laptop dashboard and people working with data"></div>
<div class="abs dots"><span class="on"></span><span></span><span></span><span></span></div>

<!-- Features -->
<h2 class="abs section-title" style="top:718px">Designed for <b>developers in need of data</b></h2>
<div class="abs underline" style="top:780px"></div>
<p class="abs intro">As a data scientist or engineer you always are looking for getting more data in with more efficiency. This is exactly what The Loomfield is making possible for you</p>

<svg class="abs" style="left:355px;top:880px" width="490" height="460" viewBox="0 0 490 460">
  <circle cx="245" cy="225" r="222" fill="none" stroke="var(--ring)" stroke-width="2"/>
  <circle cx="245" cy="217" r="184" fill="#ffffff" stroke="#c9d7e6" stroke-width="4"/>
  <circle cx="23" cy="140" r="4" fill="#7f94b3"/>
  <circle cx="31" cy="310" r="4" fill="#7f94b3"/>
  <circle cx="470" cy="145" r="4" fill="#7f94b3"/>
  <circle cx="458" cy="313" r="4" fill="#7f94b3"/>
</svg>
<div class="abs center-art" role="img" aria-label="Isometric illustration of a data city with charts, servers and people"></div>

<div class="abs feat-icon light" style="left:374px;top:911px">
  <svg width="36" height="36" viewBox="0 0 36 36" fill="none" stroke="#fff" stroke-width="1.8"><ellipse cx="18" cy="10" rx="8" ry="3"/><path d="M10 10v14c0 1.7 3.6 3 8 3s8-1.3 8-3V10"/><path d="M10 17c0 1.7 3.6 3 8 3s8-1.3 8-3"/></svg>
</div>
<div class="abs feat-icon dark" style="left:754px;top:911px">
  <svg width="36" height="36" viewBox="0 0 36 36" fill="none" stroke="#fff" stroke-width="1.8"><rect x="4" y="6" width="22" height="16" rx="2"/><circle cx="25" cy="24" r="5"/><path d="M25 16v3M25 29v3M17 24h3M30 24h3"/></svg>
</div>
<div class="abs feat-icon dark" style="left:332px;top:1068px">
  <svg width="36" height="36" viewBox="0 0 36 36" fill="none" stroke="#fff" stroke-width="1.8"><circle cx="13" cy="13" r="5"/><circle cx="24" cy="24" r="5"/><path d="M13 4v3M13 19v3M4 13h3M19 13h3M24 15v3M24 30v3M15 24h3M30 24h3"/></svg>
</div>
<div class="abs feat-icon light" style="left:798px;top:1068px">
  <svg width="40" height="36" viewBox="0 0 40 36" fill="none" stroke="#fff" stroke-width="1.8"><path d="M20 4l16 8-16 8-16-8z"/><path d="M4 18l16 8 16-8M4 24l16 8 16-8"/><text x="20" y="15" font-size="8" font-family="Roboto,sans-serif" fill="#fff" stroke="none" text-anchor="middle" font-weight="700">SDK</text></svg>
</div>
<div class="abs feat-icon light" style="left:395px;top:1229px">
  <svg width="36" height="36" viewBox="0 0 36 36" fill="none" stroke="#fff" stroke-width="1.8"><circle cx="18" cy="18" r="12"/><path d="M8 14c4 1 6 4 5 8M20 7c0 4 4 5 7 4M22 29c0-4 3-6 7-5"/></svg>
</div>
<div class="abs feat-icon dark" style="left:728px;top:1229px">
  <svg width="36" height="36" viewBox="0 0 36 36" fill="none" stroke="#fff" stroke-width="1.8"><rect x="7" y="5" width="18" height="24" rx="2"/><path d="M11 11h10M11 16h6"/><circle cx="23" cy="24" r="5"/><path d="M27 28l4 4"/></svg>
</div>

<div class="abs feat right" style="left:40px;top:906px;width:313px">
  <h3>Many Sources</h3>
  <p>Public data comes from many sources, all with their own data format and interface.</p>
</div>
<div class="abs feat" style="left:846px;top:901px;width:250px">
  <h3>Automate</h3>
  <p>Use the latest public data in your data pipeline as the loomfield makes daily updates to the data.</p>
</div>
<div class="abs feat right" style="left:63px;top:1056px;width:250px">
  <h3>Integrate</h3>
  <p>Use the loomfield API to combine Public data with your own comapny data and create value for your business.</p>
</div>
<div class="abs feat" style="left:891px;top:1069px;width:250px">
  <h3>The Loomfield SDK</h3>
  <p>Use our SDK to access our data without any knowledge of our API.</p>
</div>
<div class="abs feat right" style="left:120px;top:1222px;width:254px">
  <h3>Regional</h3>
  <p>Do you need regional information in your pipeline ? The loomfield provides public data up to community level.</p>
</div>
<div class="abs feat" style="left:821px;top:1219px;width:310px">
  <h3>Tracable</h3>
  <p>For all data we give you the legends as well as the sources from which we retrieve the data. So you always know what the data is exactly about.</p>
</div>

<a class="abs btn-pill btn-start">Get Started Now</a>

<!-- Blog -->
<div class="abs blog-bg"></div>
<h2 class="abs section-title" style="top:1552px">Latest <b>Blog</b></h2>
<div class="abs underline" style="top:1614px"></div>

<article class="abs card" style="left:102px">
  <div class="photo" role="img" aria-label="Photo of a team discussing data at a desktop computer"></div>
  <div class="body">
    <time>Nov 11, 2024</time>
    <h4>Lorem ipsum dolor sit amet, consectetur<br>adipiscing elit, sed do eiusmod</h4>
    <a class="more">READ FULL BLOG <svg width="14" height="8" viewBox="0 0 14 8"><path d="M0 4h12M9 1l3 3-3 3" stroke="currentColor" stroke-width="1.6" fill="none"/></svg></a>
  </div>
</article>
<article class="abs card" style="left:440px">
  <div class="photo warm" role="img" aria-label="Photo of two colleagues looking at a tablet in an office"></div>
  <div class="body">
    <time>Nov 11, 2024</time>
    <h4>Lorem ipsum dolor sit amet, consectetur<br>adipiscing elit, sed do eiusmod</h4>
    <a class="more">READ FULL BLOG <svg width="14" height="8" viewBox="0 0 14 8"><path d="M0 4h12M9 1l3 3-3 3" stroke="currentColor" stroke-width="1.6" fill="none"/></svg></a>
  </div>
</article>
<article class="abs card" style="left:778px">
  <div class="photo cool" role="img" aria-label="Photo of an engineer with a laptop in a server room"></div>
  <div class="body">
    <time>Nov 11, 2024</time>
    <h4>Lorem ipsum dolor sit amet, consectetur<br>adipiscing elit, sed do eiusmod</h4>
    <a class="more">READ FULL BLOG <svg width="14" height="8" viewBox="0 0 14 8"><path d="M0 4h12M9 1l3 3-3 3" stroke="currentColor" stroke-width="1.6" fill="none"/></svg></a>
  </div>
</article>

<!-- Footer -->
<svg class="abs footer-shape" width="1200" height="517" viewBox="0 0 1200 517">
  <defs>
    <linearGradient id="footGrad" x1="0" y1="1" x2="1" y2="0">
      <stop offset="0" stop-color="#0d57bf"/>
      <stop offset="1" stop-color="#4cbdf0"/>
    </linearGradient>
  </defs>
  <path d="M0 115 C250 20 500 90 700 80 C900 70 1080 30 1200 0 L1200 517 L0 517 Z" fill="url(#footGrad)"/>
</svg>

<section class="abs newsletter">
  <h2>Sign Up For<br>Our Newsletter</h2>
  <div class="subscribe"><span>Email Address</span><b>SUBSCRIBE</b></div>
</section>

<div class="abs f-brand">
  <h5>The <b>Loomfield</b></h5>
  <p>The Loomfield was created to simplify access to public data and save you countless hours of manual collection</p>
</div>
<div class="abs f-divider" style="left:431px"></div>
<div class="abs f-divider" style="left:629px"></div>
<div class="abs f-divider" style="left:882px"></div>

<div class="abs f-col" style="left:431px">
  <h6>Navigation</h6>
  <ul><li>Introduction</li><li>The datamodels</li><li>The API</li><li>The SDK</li></ul>
</div>
<div class="abs f-col" style="left:629px">
  <h6>The Company</h6>
  <ul><li>About</li><li>Frequently Asked Questions</li><li>Privacy Policy</li><li>Cookie Policy</li><li>Terms of Service</li></ul>
</div>
<div class="abs f-col" style="left:882px">
  <h6>Contact Us</h6>
  <ul><li>Email:</li><li class="mail">info@the-loomfield.io</li></ul>
  <div class="social"><span></span><span></span></div>
</div>

<div class="abs f-rule"></div>
<p class="abs copyright">© 2024 The Loomfield. All rights reserved.</p>

</body>
</html>
```